Buisness card

**Front Side:**

**[Your Company Logo]**
**Steadfast Upkeep Industrial**
*Keeping Your Equipment Running Smoothly*

**Contact Information:**
- **Name:** [darren Whitlow
- **Title:** [owner
- **Phone:** [8025196047
- **Email:** darren@sukrn.com

**Back Side:**

**Services Offered:**
- Routine Inspections
- Equipment Maintenance
- Emergency Repairs
- Consultation Services
- New installs
Tag line
Be proactive not reactive

```html
<!DOCTYPE html>
<html lang="en">
<head>
<meta charset="utf-8">
<title>Steadfast Upkeep Industrial – Business Card</title>
<link href="https://fonts.googleapis.com/css2?family=Montserrat:wght@400;600;700;800&display=swap" rel="stylesheet">
<style>
  :root {
    --navy: #0a2a6e;
    --blue: #1e6fe0;
    --sky: #2fb8f0;
    --red: #e02020;
    --white: #ffffff;
    --ink: #1a1f36;
    --bg: #2a2a2c;
  }
  * { margin: 0; padding: 0; box-sizing: border-box; }
  html, body { width: 1200px; height: 875px; overflow: hidden; }
  body {
    background: var(--bg);
    font-family: "Montserrat", sans-serif;
    display: flex; flex-direction: column; align-items: center; justify-content: center;
    gap: 40px;
  }
  .card {
    width: 640px; height: 366px; border-radius: 22px;
    position: relative; overflow: hidden;
    box-shadow: 0 18px 40px rgba(0,0,0,.45);
  }
  .card--back { background: var(--navy); color: var(--white); }
  .card--front { background: var(--white); color: var(--navy); }
  .card--front .bottom-band {
    position: absolute; left: 0; right: 0; bottom: 0; height: 14px; background: var(--navy);
  }
  .brand { display: flex; align-items: center; gap: 22px; }
  .brand-mark { width: 118px; height: 118px; border-radius: 50%; flex: none; }
  .card--back .brand-mark { background: var(--white); }
  .card--front .brand-mark { background: var(--navy); }
  .brand-name {
    font-weight: 800; font-size: 30px; line-height: 1.08; text-transform: uppercase;
    letter-spacing: .5px;
  }
  .card--back .brand-name { color: var(--white); }
  .card--front .brand-name { color: var(--blue); }
  .tagline { font-weight: 600; text-transform: uppercase; margin-top: 8px; }
  .card--back .tagline { font-size: 17px; letter-spacing: .5px; }
  .card--front .tagline { font-size: 12px; color: var(--ink); letter-spacing: .3px; }

  .card--back .brand { position: absolute; left: 44px; top: 44px; }
  .services { position: absolute; left: 44px; right: 40px; bottom: 44px; }
  .services-title { font-weight: 800; font-size: 26px; letter-spacing: 1px; margin-bottom: 10px; }
  .services-row {
    list-style: none; display: flex; column-gap: 10px; margin-top: 6px;
    font-size: 13.5px; font-weight: 600; text-transform: uppercase; letter-spacing: .3px;
  }
  .services-row li { display: flex; align-items: center; gap: 10px; white-space: nowrap; }
  .services-row li + li::before {
    content: ""; width: 7px; height: 7px; border-radius: 50%; background: var(--sky);
  }

  .card--front .brand { position: absolute; left: 40px; top: 44px; }
  .person { position: absolute; left: 40px; bottom: 58px; }
  .person-name { font-weight: 800; font-size: 30px; letter-spacing: .8px; text-transform: uppercase; color: var(--navy); white-space: nowrap; }
  .person-title { font-size: 18px; font-weight: 400; color: var(--blue); margin-top: 2px; }
  .divider { position: absolute; left: 420px; bottom: 56px; width: 2px; height: 92px; background: var(--red); }
  .contacts { position: absolute; left: 438px; bottom: 60px; list-style: none; }
  .contacts li { display: flex; align-items: center; gap: 10px; font-size: 14px; color: var(--ink); line-height: 28px; white-space: nowrap; }
  .contacts svg { width: 14px; height: 14px; fill: var(--blue); flex: none; }
</style>
</head>
<body>

  <section class="card card--back" aria-label="Card back">
    <div class="brand">
      <div class="brand-mark"></div>
      <div>
        <div class="brand-name">Steadfast Upkeep<br>Industrial</div>
        <div class="tagline">Be proactive not reactive</div>
      </div>
    </div>
    <div class="services">
      <h2 class="services-title">SERVICES OFFERED:</h2>
      <ul class="services-row">
        <li>Routine Inspections</li>
        <li>Equipment Maintenance</li>
      </ul>
      <ul class="services-row">
        <li>Emergency Repairs</li>
        <li>Consultation Services</li>
        <li>New Installs</li>
      </ul>
    </div>
  </section>

  <section class="card card--front" aria-label="Card front">
    <div class="brand">
      <div class="brand-mark"></div>
      <div>
        <div class="brand-name">Steadfast Upkeep<br>Industrial</div>
        <div class="tagline">Keeping your equipment running smoothly</div>
      </div>
    </div>
    <div class="person">
      <div class="person-name">Darren Whitlow</div>
      <div class="person-title">Owner</div>
    </div>
    <div class="divider"></div>
    <ul class="contacts">
      <li>
        <svg viewBox="0 0 24 24" aria-hidden="true"><path d="M6.6 10.8a15.1 15.1 0 0 0 6.6 6.6l2.2-2.2c.3-.3.7-.4 1-.2 1.1.4 2.3.6 3.6.6.6 0 1 .4 1 1V20c0 .6-.4 1-1 1A17 17 0 0 1 3 4c0-.6.4-1 1-1h3.5c.6 0 1 .4 1 1 0 1.3.2 2.5.6 3.6.1.3 0 .7-.2 1z"/></svg>
        8025196047
      </li>
      <li>
        <svg viewBox="0 0 24 24" aria-hidden="true"><path d="M2 5h20v14H2zm2 2v.5l8 5 8-5V7l-8 5z"/></svg>
        darren@sukrn.com
      </li>
      <li>
        <svg viewBox="0 0 24 24" aria-hidden="true"><path d="M12 2a10 10 0 1 0 0 20 10 10 0 0 0 0-20zm0 2c1.2 1.4 2 3.6 2.2 7H9.8C10 7.6 10.8 5.4 12 4zM4.1 13h3.7c.1 2.5.7 4.6 1.6 6.2A8 8 0 0 1 4.1 13zm0-2a8 8 0 0 1 5.3-6.2C8.5 6.4 7.9 8.5 7.8 11zm7.9 9c-1.2-1.4-2-3.6-2.2-7h4.4c-.2 3.4-1 5.6-2.2 7zm2.6-.8c.9-1.6 1.5-3.7 1.6-6.2h3.7a8 8 0 0 1-5.3 6.2zM16.2 11c-.1-2.5-.7-4.6-1.6-6.2A8 8 0 0 1 19.9 11z"/></svg>
        sukrn.com
      </li>
    </ul>
    <div class="bottom-band"></div>
  </section>

</body>
</html>
```